Brand new letterhead, business card, email signature etc.

We are a financial company in London, UK. Our website is www.quorvane.com. We're wanting a complete remodel of the company colours, letter head, business cards, email signatures, etc. Looking to keep the same font for the company name. I have upload a colour palette that we want to work with. We're looking for company letterhead for outgoing letters/ correspondence, letterhead for internal documentation, email signatures, e-letters. etc. Ultimately we will redesign the entire website also. It is important that our clients get a strong, secure, warm, trustworthy, solid feeling and first impression.
Updates

Designs look the same

Target Market(s)

Institutional investors, (ultra) high net worth individuals

Industry/Entity Type

Finance, Invesments banking.

Font styles to use
Other font styles liked:
• Current font is "Champagne & Limousines"

Requirements
Must have
• Must use the colours provided on the PDF uploaded to the portal. The purple = main colour. The red = accent colour.
Nice to have
• Nice to use same font as now for the company name "Marlowin". Font is "Champagne & Limousines". Nice to have some reference to the old logo flower, but only subtle.
Should not have
• Do not use the colour red from our website. Use the colours provided on the colour palette PDF that I uploaded in the portal.

```html
<!DOCTYPE html>
<html lang="en">
<head>
<meta charset="utf-8">
<title>Marlowin Stationery Suite</title>
<link href="https://fonts.googleapis.com/css2?family=Josefin+Sans:wght@300&family=Montserrat:wght@400;700&display=swap" rel="stylesheet">
<style>
  :root {
    --brand: #3a1f4d;
    --brand-light: #52336a;
    --ink: #2b1a38;
    --paper: #ffffff;
    --stage: #efefef;
    --accent: #c41e3a;
    --text-light: #f4f0f7;
  }
  * { box-sizing: border-box; margin: 0; padding: 0; }
  html, body { width: 1200px; height: 1200px; overflow: hidden; }
  body {
    background: var(--stage);
    font-family: "Montserrat", Arial, sans-serif;
    position: relative;
    color: var(--ink);
  }
  .wordmark {
    font-family: "Josefin Sans", "Helvetica Neue", sans-serif;
    font-weight: 300;
    text-transform: uppercase;
    letter-spacing: 0.1em;
    line-height: 1;
    display: flex;
    align-items: center;
    white-space: nowrap;
  }
  .wordmark .mark-square {
    display: inline-block;
    border: 1.5px solid currentColor;
    margin-right: 0.4em;
    flex: none;
  }
  .icon { width: 11px; height: 11px; flex: none; }
  .contact-row { display: flex; align-items: center; justify-content: flex-end; gap: 8px; white-space: nowrap; }
  .address-block { display: flex; justify-content: flex-end; gap: 8px; white-space: nowrap; }
  .address-block .lines { text-align: right; }

  /* Letterhead */
  .letterhead {
    position: absolute; left: 226px; top: 72px; width: 746px; height: 1057px;
    background: var(--paper);
  }
  .letterhead .wordmark { position: absolute; left: 52px; top: 60px; font-size: 38px; color: var(--brand); }
  .letterhead .mark-square { width: 82px; height: 82px; }
  .letterhead .watermark {
    position: absolute; left: 0; top: 200px; width: 560px; height: 820px;
    background: radial-gradient(ellipse at 45% 50%, #f5f2f7 0%, rgba(255,255,255,0) 70%);
  }
  .letterhead .footer-contact {
    position: absolute; right: 28px; top: 902px; font-size: 15.5px; line-height: 1.2; color: var(--ink);
  }
  .letterhead .footer-contact .contact-row + .contact-row { margin-top: 4px; }
  .letterhead .footer-contact .address-block { margin-top: 18px; }
  .letterhead .icon { width: 13px; height: 13px; color: var(--brand); }

  /* Business cards */
  .card {
    position: absolute; left: 709px; width: 435px; height: 256px;
    background: var(--brand); color: var(--text-light);
  }
  .card-details { top: 281px; }
  .card-brand { top: 679px; }
  .card-details .brand-art {
    position: absolute; left: 40px; top: 40px; width: 180px; height: 180px;
    background: radial-gradient(circle at 50% 50%, var(--brand-light) 0%, #45285a 60%, var(--brand) 100%);
  }
  .card-details .info {
    position: absolute; right: 26px; top: 67px; text-align: right; font-size: 11px; line-height: 1.3;
  }
  .person-name { font-weight: 700; color: var(--accent); font-size: 15px; letter-spacing: 0.02em; text-transform: uppercase; white-space: nowrap; }
  .card .person-name { color: #e8546c; }
  .person-role { font-size: 11.5px; margin-top: 2px; white-space: nowrap; }
  .card-details .contacts { margin-top: 24px; }
  .card-details .address-block { margin-top: 14px; }
  .card-details .icon { color: #e8546c; }
  .card-brand .wordmark {
    position: absolute; left: 72px; top: 95px; font-size: 36px; color: var(--text-light);
  }
  .card-brand .mark-square { width: 68px; height: 68px; }

  /* Email signature */
  .email-signature {
    position: absolute; left: 71px; top: 797px; width: 600px; height: 138px;
    background: var(--paper);
  }
  .email-signature .name-tab {
    position: absolute; right: 0; top: 0; width: 249px; height: 52px;
    background: var(--accent); color: var(--paper);
    border-top-left-radius: 40px 52px;
    text-align: right; padding: 14px 10px 0 0;
  }
  .email-signature .person-name { color: var(--paper); font-size: 13.5px; }
  .email-signature .person-role { font-size: 11px; margin-top: 0; }
  .email-signature .wordmark { position: absolute; left: 18px; top: 48px; font-size: 24px; color: var(--brand); }
  .email-signature .mark-square { width: 48px; height: 48px; }
  .email-signature .contacts {
    position: absolute; left: 296px; top: 70px; font-size: 10.5px; line-height: 1.5; color: var(--ink);
  }
  .email-signature .address-block {
    position: absolute; right: 35px; top: 70px; font-size: 10.5px; line-height: 1.35; color: var(--ink);
  }
  .email-signature .icon { width: 10px; height: 10px; color: var(--brand); }
</style>
</head>
<body>

<svg width="0" height="0" style="position:absolute">
  <defs>
    <symbol id="icon-mail" viewBox="0 0 16 16"><rect x="1" y="3" width="14" height="10" fill="currentColor"/><path d="M1 3.5 8 9l7-5.5" fill="none" stroke="#ffffff" stroke-width="1.3"/></symbol>
    <symbol id="icon-globe" viewBox="0 0 16 16"><circle cx="8" cy="8" r="7" fill="none" stroke="currentColor" stroke-width="1.5"/><ellipse cx="8" cy="8" rx="3" ry="7" fill="none" stroke="currentColor" stroke-width="1.2"/><path d="M1 8h14" stroke="currentColor" stroke-width="1.2"/></symbol>
    <symbol id="icon-pin" viewBox="0 0 16 16"><path d="M8 1a5 5 0 0 0-5 5c0 4 5 9 5 9s5-5 5-9a5 5 0 0 0-5-5z" fill="none" stroke="currentColor" stroke-width="1.6"/><circle cx="8" cy="6" r="1.8" fill="currentColor"/></symbol>
  </defs>
</svg>

<section class="letterhead">
  <div class="watermark" role="img" aria-label="Faint brand decoration area"></div>
  <div class="wordmark"><span class="mark-square"></span>Marlowin</div>
  <div class="footer-contact">
    <div class="contact-row">info@quorvane.com <svg class="icon"><use href="#icon-mail"/></svg></div>
    <div class="contact-row">www.quorvane.com <svg class="icon"><use href="#icon-globe"/></svg></div>
    <div class="address-block">
      <div class="lines">9th Floor<br>18 Aldgate Row<br>London<br>EC3N 2LT</div>
      <svg class="icon"><use href="#icon-pin"/></svg>
    </div>
  </div>
</section>

<section class="card card-details">
  <div class="brand-art" role="img" aria-label="Line illustration of a flower in white with red stamen tips"></div>
  <div class="info">
    <div class="person-name">Elliot Branwell</div>
    <div class="person-role">Executive Director</div>
    <div class="contacts">
      <div class="contact-row">info@quorvane.com <svg class="icon"><use href="#icon-mail"/></svg></div>
      <div class="contact-row">www.quorvane.com <svg class="icon"><use href="#icon-globe"/></svg></div>
    </div>
    <div class="address-block">
      <div class="lines">9th Floor<br>18 Aldgate Row<br>London<br>EC3N 2LT</div>
      <svg class="icon"><use href="#icon-pin"/></svg>
    </div>
  </div>
</section>

<section class="card card-brand">
  <div class="wordmark"><span class="mark-square"></span>Marlowin</div>
</section>

<section class="email-signature">
  <div class="name-tab">
    <div class="person-name">Elliot Branwell</div>
    <div class="person-role">Executive Director</div>
  </div>
  <div class="wordmark"><span class="mark-square"></span>Marlowin</div>
  <div class="contacts">
    <div class="contact-row">info@quorvane.com <svg class="icon"><use href="#icon-mail"/></svg></div>
    <div class="contact-row">www.quorvane.com <svg class="icon"><use href="#icon-globe"/></svg></div>
  </div>
  <div class="address-block">
    <div class="lines">9th Floor<br>18 Aldgate Row<br>London<br>EC3N 2LT</div>
    <svg class="icon"><use href="#icon-pin"/></svg>
  </div>
</section>

</body>
</html>
```